Require modern interface design for our website.

We are looking for a redesign of our website interface. The interface and the look and feel needs to be modern and seamless. Designer must be able to integrate with the backend PHP and Java. Please try utilise logo and colours where possible don't go too drastic. We utilise this site for learning and training purposes so please keep in line with that objective.

Target Market(s)

Education

Industry/Entity Type

Education

Number of Pages Required

5+ page

Font styles to use
Sans Serif

Requirements
Must have
• Innovative and modern look, logo to be incorporated.
Nice to have
• Good use of colours
Should not have
• Lack of creativity

```html
<!DOCTYPE html>
<html lang="en">
<head>
<meta charset="utf-8">
<title>Brightlearn – Online Courses</title>
<link href="https://fonts.googleapis.com/css2?family=Open+Sans:wght@400;600;700&family=Raleway:wght@300;400;600&display=swap" rel="stylesheet">
<style>
:root{
  --blue:#1e8fe6;
  --blue-dark:#1672bd;
  --ink:#333;
  --muted:#777;
  --light:#f4f4f4;
  --line:#e2e2e2;
  --footer:#2a2a2a;
  --footer-deep:#1c1c1c;
  --white:#fff;
}
*{box-sizing:border-box;margin:0;padding:0}
html,body{width:1200px;height:2304px;overflow:hidden}
body{font-family:"Open Sans",Arial,sans-serif;color:var(--ink);background:var(--white);position:relative}
.section{position:absolute;left:0;width:1200px}
.heading-caps{font-family:"Raleway",Arial,sans-serif;font-variant:small-caps;font-weight:400;letter-spacing:2px}
p{font-size:13px;line-height:20px;color:var(--muted)}
.btn{display:inline-block;background:var(--blue);color:var(--white);font-size:12px;padding:7px 18px;border-radius:2px;text-decoration:none}

/* hero */
.hero{top:0;height:500px;background:linear-gradient(100deg,#d8d4cd 0%,#efece7 30%,#f6f3ee 55%,#d9c9b4 78%,#b7a48c 100%)}
.search{position:absolute;left:360px;top:180px;width:480px;height:50px;display:flex}
.search-field{flex:1;background:var(--white);border:1px solid var(--line);font-size:15px;color:#888;padding:14px 16px}
.search-btn{width:52px;background:var(--blue);display:flex;align-items:center;justify-content:center}
.hero-title{position:absolute;top:248px;width:100%;text-align:center;color:var(--blue);font-size:46px}

/* nav */
.nav{top:500px;height:60px;background:var(--white);border-bottom:1px solid var(--line);box-shadow:0 2px 6px rgba(0,0,0,.06)}
.logo{position:absolute;left:110px;top:16px;font-size:22px;font-weight:700;color:var(--blue);display:flex;align-items:center;gap:8px}
.logo-dot{width:14px;height:14px;border-radius:50%;background:var(--blue)}
.menu{position:absolute;right:110px;top:21px;display:flex;font-size:13px}
.menu a{color:var(--ink);text-decoration:none;padding:0 14px;border-left:1px solid var(--line)}
.menu a:first-child{border-left:none}

/* how */
.how{top:570px;height:400px}
.how-title{position:absolute;top:12px;left:110px;width:720px;text-align:center;font-size:46px;color:#444}
.how-sub{position:absolute;top:74px;left:110px;width:720px;text-align:center;font-size:12px}
.how-copy{position:absolute;left:110px;top:130px;width:720px}
.how-copy h3{font-family:"Raleway",Arial,sans-serif;font-weight:600;font-size:19px;color:#444;margin-bottom:18px;white-space:nowrap}
.how-copy p{margin-bottom:14px}
.student-photo{position:absolute;left:870px;top:40px;width:230px;height:350px;background:linear-gradient(180deg,#f2f2f2,#e6dccd 50%,#c9a95d 80%,#f3f3f3)}

/* courses */
.courses{top:980px;height:340px;background:linear-gradient(180deg,#e9e9e9,#dcdcdc 50%,#ececec)}
.courses-title{position:absolute;top:24px;width:100%;text-align:center;font-size:40px;color:#444}
.course{position:absolute;top:100px;width:210px;height:200px;text-align:center}
.course h4{font-weight:400;font-size:14px;letter-spacing:1px;color:#555;margin:10px 0 8px}
.course p{font-size:11px;line-height:16px;color:#666;height:48px}
.course .btn{position:absolute;left:50%;top:170px;transform:translateX(-50%);background:#777;font-size:11px;padding:5px 14px}
.course .btn.active{background:var(--blue)}

/* information */
.info{top:1330px;height:300px}
.video{position:absolute;left:112px;top:30px;width:408px;height:250px;background:linear-gradient(135deg,#3a3a3a,#6d6a64 55%,#2a2a2a)}
.info-copy{position:absolute;left:560px;top:30px;width:530px}
.info-copy .kicker{color:var(--blue);font-size:38px}
.info-copy h3{font-family:"Raleway",Arial,sans-serif;font-weight:300;font-size:32px;letter-spacing:1px;color:#444;margin:2px 0 14px}
.info-copy p{margin-bottom:12px}

/* blog */
.blog{top:1630px;height:330px;background:linear-gradient(180deg,#3c3c3c,#1e1e1e 60%,#2c2c2c)}
.blog-title{position:absolute;top:16px;width:100%;text-align:center;color:var(--white);font-size:38px}
.avatar{position:absolute;left:540px;top:70px;width:120px;height:120px;border-radius:50%;background:linear-gradient(180deg,#b8b2aa,#6e6862);border:3px solid var(--white)}
.blog-text{position:absolute;left:110px;top:214px;width:980px;text-align:center;color:#ddd}
.blog-more{position:absolute;top:278px;width:100%;text-align:center;color:var(--blue);font-size:15px}

/* footer */
.footer{top:1960px;height:300px;background:var(--footer)}
.foot-col{position:absolute;top:30px;color:#ccc;font-size:12px}
.foot-col h5{color:var(--blue);font-family:"Raleway",Arial,sans-serif;font-variant:small-caps;font-weight:400;font-size:18px;letter-spacing:1px;margin-bottom:14px}
.foot-col li{list-style:none;line-height:24px;display:flex;align-items:center;gap:8px}
.foot-col li::before{content:"›";color:#888}
.foot-col.plain li::before{content:none}
.icon-box{width:18px;height:18px;border:1px solid #777;background:#3a3a3a;display:inline-block}
.copyright{top:2260px;height:44px;background:var(--footer-deep);color:#aaa;font-size:12px;text-align:center;line-height:44px}
</style>
</head>
<body>

<header class="section hero" role="img" aria-label="Photo of a student working on a laptop in a bright study space">
  <div class="search">
    <div class="search-field">Search Course</div>
    <div class="search-btn">
      <svg width="20" height="20" viewBox="0 0 20 20"><circle cx="8" cy="8" r="6" fill="none" stroke="#fff" stroke-width="2.2"/><line x1="12.5" y1="12.5" x2="18" y2="18" stroke="#fff" stroke-width="2.4"/></svg>
    </div>
  </div>
  <h1 class="hero-title heading-caps">We have the largest collection of courses</h1>
</header>

<nav class="section nav">
  <div class="logo"><span class="logo-dot"></span>Brightlearn</div>
  <div class="menu">
    <a>Home</a><a>About</a><a>Courses</a><a>Blog</a><a>Contact</a><a>Login / Register</a>
  </div>
</nav>

<section class="section how">
  <h2 class="how-title heading-caps">How does it work?</h2>
  <p class="how-sub">Pick a course, learn at your own pace and earn a certificate once you finish.</p>
  <div class="how-copy">
    <h3>Contrary to popular belief, Lorem Ipsum is not simply random text.</h3>
    <p>Our courses are written by working teachers and trainers who know what learners need. Every lesson is short, clear and built around practical tasks, so you can study in small steps and still see real progress each week. You choose when and where to learn.</p>
    <p>Lessons include videos, reading notes, quizzes and assignments. Tutors review your work and give helpful feedback, and the forum lets you ask questions and share ideas with other students taking the same course.</p>
    <a class="btn">Read More</a>
  </div>
  <div class="student-photo" role="img" aria-label="Photo of a smiling student holding yellow folders"></div>
</section>

<section class="section courses">
  <h2 class="courses-title heading-caps">Courses</h2>

  <div class="course" style="left:105px">
    <svg width="60" height="50" viewBox="0 0 60 50"><rect x="22" y="4" width="16" height="26" rx="8" fill="#666"/><path d="M15 22a15 15 0 0 0 30 0" fill="none" stroke="#666" stroke-width="3"/><line x1="30" y1="37" x2="30" y2="46" stroke="#666" stroke-width="3"/></svg>
    <h4>AUDIO PODCAST</h4>
    <p>Listen to weekly talks from our tutors on the go and revise key topics wherever you are.</p>
    <a class="btn">Read More</a>
  </div>

  <div class="course" style="left:380px">
    <svg width="60" height="50" viewBox="0 0 60 50"><path d="M6 10h20a4 4 0 0 1 4 4v30a4 4 0 0 0-4-4H6z" fill="#1e8fe6"/><path d="M54 10H34a4 4 0 0 0-4 4v30a4 4 0 0 1 4-4h20z" fill="#1e8fe6"/></svg>
    <h4 style="color:#1e8fe6">HOME ASSIGNMENTS</h4>
    <p>Practical tasks you complete at home, marked by tutors with clear feedback and tips.</p>
    <a class="btn active">Read More</a>
  </div>

  <div class="course" style="left:627px">
    <svg width="60" height="50" viewBox="0 0 60 50"><rect x="8" y="32" width="8" height="14" fill="#666"/><rect x="20" y="24" width="8" height="22" fill="#666"/><rect x="32" y="18" width="8" height="28" fill="#666"/><rect x="44" y="10" width="8" height="36" fill="#666"/><polyline points="8,24 22,14 34,16 50,4" fill="none" stroke="#666" stroke-width="2"/></svg>
    <h4>BUSINESS STUDIES</h4>
    <p>Learn the basics of finance, marketing and management with real case studies.</p>
    <a class="btn">Read More</a>
  </div>

  <div class="course" style="left:875px">
    <svg width="60" height="50" viewBox="0 0 60 50"><circle cx="30" cy="25" r="19" fill="none" stroke="#666" stroke-width="3"/><path d="M11 25h38M30 6v38" stroke="#666" stroke-width="2"/></svg>
    <h4>SPORTS ACTIVITIES</h4>
    <p>Coaching courses and fitness plans to keep body and mind active while you study.</p>
    <a class="btn">Read More</a>
  </div>
</section>

<section class="section info">
  <div class="video" role="img" aria-label="Video still introducing the course method"></div>
  <div class="info-copy">
    <div class="kicker heading-caps">Information</div>
    <h3>OUR METHODOLOGY</h3>
    <p>We believe every learner moves at a different speed. That is why each course is split into short modules with clear goals, quick checks and regular tutor contact.</p>
    <p>After every module you get a summary of what you learned and what to practise next, so you always know where you stand and how close you are to your goal.</p>
    <a class="btn">Find Out More</a>
  </div>
</section>

<section class="section blog" role="img" aria-label="Dark photo of a desk with notebooks behind the blog section">
  <h2 class="blog-title heading-caps">Blog</h2>
  <div class="avatar" role="img" aria-label="Portrait of the blog author"></div>
  <p class="blog-text">Read the latest stories from our teaching team: study tips, new course launches, interviews with graduates and ideas for staying focused while learning from home. New posts arrive every week, so check back often and join the discussion.</p>
  <div class="blog-more">Read More</div>
</section>

<footer class="section footer">
  <div class="foot-col" style="left:120px">
    <h5>Company</h5>
    <ul><li>About</li><li>Privacy</li><li>Terms and Conditions</li><li>News</li><li>Press</li><li>Be a teacher</li><li>Help</li></ul>
  </div>
  <div class="foot-col" style="left:370px">
    <h5>Options</h5>
    <ul><li>PRICES</li><li>FAQ</li><li>GROUP CLASSES</li><li>WEBINARS</li><li>PRIVATE LANGUAGE LESSONS</li></ul>
  </div>
  <div class="foot-col plain" style="left:630px">
    <h5>Contact Us</h5>
    <ul>
      <li><svg width="14" height="14" viewBox="0 0 14 14"><path d="M7 1a4 4 0 0 1 4 4c0 3-4 8-4 8S3 8 3 5a4 4 0 0 1 4-4z" fill="#bbb"/></svg>12 Example Road, Springfield</li>
      <li style="margin-top:8px"><svg width="14" height="14" viewBox="0 0 14 14"><path d="M3 1l3 3-2 2a8 8 0 0 0 4 4l2-2 3 3-2 2C6 13 1 8 1 3z" fill="#bbb"/></svg>Call Now: 000-000-0000</li>
      <li style="margin-top:8px"><svg width="14" height="14" viewBox="0 0 14 14"><rect x="1" y="3" width="12" height="8" fill="none" stroke="#bbb"/><polyline points="1,3 7,8 13,3" fill="none" stroke="#bbb"/></svg>Email: hello@brightlearn.example</li>
    </ul>
  </div>
  <div class="foot-col plain" style="left:890px">
    <h5>Social Networks</h5>
    <ul><li><span class="icon-box"></span>Community</li><li><span class="icon-box"></span>News Feed</li><li><span class="icon-box"></span>Careers</li><li><span class="icon-box"></span>Video Channel</li><li><span class="icon-box"></span>Circles</li></ul>
  </div>
</footer>
<div class="section copyright">© brightlearn.example All Right Reserved</div>

</body>
</html>
```